Licensed School Psychologist Business Card Design (may be single or double sided)

In an empathetic and nurturing environment, I conduct comprehensive psycho-educational evaluations for children and adolescents who may be experiencing academic, social/emotional challenges, and stressors in their lives. Given the collection of data and information, recommendations, supports, and strategies are created and tailored to the strengths and weaknesses of the children/adolescents as well as their families.

Industry/Entity Type

Business

Contact Information for Business Card

Bright-Path Learning Assessments
Mona Velkrist, MEd; MA
Licensed School Psychologist
482 Tarnby Crescent, Suite #3
Harlowmere, VA 23991
P: 757 918-2073 F: 757 918-2150

```html
<!DOCTYPE html>
<html lang="en">
<head>
<meta charset="utf-8">
<title>Bright-Path Learning Assessments — Business Card</title>
<link href="https://fonts.googleapis.com/css2?family=Open+Sans:wght@400;600;700&display=swap" rel="stylesheet">
<style>
  :root {
    --backdrop: #d9dadc;
    --card-front: #4474b8;
    --card-back: #1f74d9;
    --accent: #f4a024;
    --ink-light: #ffffff;
    --ink-soft: #e3ebf6;
  }
  * { margin: 0; padding: 0; box-sizing: border-box; }
  html, body {
    width: 1200px; height: 753px; overflow: hidden;
    background: var(--backdrop);
    font-family: "Open Sans", Arial, sans-serif;
  }
  .sheet {
    position: relative; width: 1200px; height: 753px;
    display: flex; align-items: center; justify-content: center; gap: 40px;
  }
  .card {
    position: relative; width: 520px; height: 297px; overflow: hidden;
    box-shadow: 0 6px 18px rgba(0,0,0,0.18);
  }

  /* Front side */
  .card--front { background: var(--card-front); color: var(--ink-light); }
  .stripe { position: absolute; left: 0; right: 0; height: 6px; background: var(--accent); }
  .stripe--top { top: 16px; }
  .stripe--bottom { bottom: 16px; }
  .brand { position: absolute; left: 34px; top: 84px; line-height: 1; }
  .brand__name { font-weight: 700; font-size: 26px; letter-spacing: 0.2px; }
  .brand__tagline { font-weight: 400; font-size: 16px; letter-spacing: 1.6px; margin-top: 3px; }
  .address {
    position: absolute; left: 34px; top: 160px;
    font-size: 11px; line-height: 1.45; color: var(--ink-soft);
  }
  .contacts { position: absolute; left: 34px; top: 214px; list-style: none; }
  .contacts__item {
    display: flex; align-items: center; gap: 12px;
    font-weight: 700; font-size: 15px; line-height: 24px;
  }
  .contacts__icon { width: 15px; height: 15px; fill: var(--accent); }
  .namebox {
    position: absolute; right: 0; top: 96px; width: 208px; height: 62px;
    background: var(--accent); padding: 11px 0 0 20px; line-height: 1;
  }
  .namebox__name { font-weight: 700; font-size: 20px; letter-spacing: 0.6px; }
  .namebox__title { font-size: 10px; letter-spacing: 1.6px; margin-top: 5px; padding-left: 66px; }

  /* Back side */
  .card--back { background: var(--card-back); color: var(--ink-light); }
  .frame {
    position: absolute; left: 40px; top: 36px; right: 40px; bottom: 36px;
    border: 3px solid var(--accent);
  }
  .back-brand {
    position: absolute; inset: 0; display: flex; flex-direction: column;
    align-items: center; justify-content: center; line-height: 1;
  }
  .back-brand__name { font-weight: 700; font-size: 22px; }
  .back-brand__tagline { font-size: 13px; letter-spacing: 1.4px; margin-top: 3px; }
</style>
</head>
<body>
<main class="sheet">
  <section class="card card--front" aria-label="Business card front">
    <div class="stripe stripe--top"></div>
    <div class="brand">
      <div class="brand__name">Bright-Path</div>
      <div class="brand__tagline">Learning Assessments</div>
    </div>
    <div class="namebox">
      <div class="namebox__name">Mona Velkrist</div>
      <div class="namebox__title">MED / DOCTOR</div>
    </div>
    <p class="address">
      MA Licensed School<br>
      Psychologist 482 Tarnby Crescent,<br>
      Suite #3 Harlowmere, VA 23991
    </p>
    <ul class="contacts">
      <li class="contacts__item">
        <svg class="contacts__icon" viewBox="0 0 16 16" aria-hidden="true">
          <path d="M1 6c0-2 3-4 7-4s7 2 7 4v1h-4V5.5H5V7H1z"/>
          <path d="M4 8h8l2 6H2z M8 9.5a2 2 0 1 0 0.01 0z"/>
        </svg>
        <span>757 918-2073</span>
      </li>
      <li class="contacts__item">
        <svg class="contacts__icon" viewBox="0 0 16 16" aria-hidden="true">
          <path d="M4 1h8v4H4z"/>
          <path d="M1 6h14v6h-3v-2H4v2H1z"/>
          <path d="M5 11h6v4H5z"/>
        </svg>
        <span>757 918-2150</span>
      </li>
    </ul>
    <div class="stripe stripe--bottom"></div>
  </section>

  <section class="card card--back" aria-label="Business card back">
    <div class="frame"></div>
    <div class="back-brand">
      <div class="back-brand__name">Bright-Path</div>
      <div class="back-brand__tagline">Learning Assessments</div>
    </div>
  </section>
</main>
</body>
</html>
```